Design of Labels for Harrowmere Dock Spirit bottle

Design bottle labels for Harrowmere Dock Spirit. There are three labels to design; a front, a back and a tamper band to be placed over the cork. The labels should be deigned to fit the bottle specified in the link below.
The Gin is an excellent high end premium brand Navy strength Gin 57% Vol. The bottle should evoke excellence and a romance of period of pride in the British Navy. Gin was drunk by officers in the Navy so a representation of the Officer Class should be made possibly through gold braid of a senior officer's sleeve, cap or lapel. The white ensign should also be prominent. Suggested colour themes are navy blues, grey, and white....although others schemes may be suitable. Pellick's Quay Brandy is a good example of the sort of thing we are looking for, although the design must not be so similar that it encroaches on Pellick's trade mark or copyrights. The period theme is 1900 to 1940
Bottle link: https://www.vessel-crate-supply.co.uk/Glass-bottles/350ml-flint-glass-bottle-Marlo.html
Target Market(s)
Gin Drinkers
Look and feel

```html
<!DOCTYPE html>
<html lang="en">
<head>
<meta charset="utf-8">
<title>Harrowmere Dock Spirit – Front Label</title>
<link rel="stylesheet" href="https://fonts.googleapis.com/css2?family=Playfair+Display:wght@700;900&family=Pinyon+Script&family=Oswald:wght@400;500&display=swap">
<style>
  :root {
    --backdrop: #c8cbd6;
    --label-white: #f4f4f2;
    --navy: #1f2535;
    --gold: #c9a649;
    --gold-soft: #d9bd6a;
    --rope-grey: #d8d9dc;
    --tag-grey: #55575c;
  }
  * { margin: 0; padding: 0; box-sizing: border-box; }
  html, body {
    width: 1200px; height: 1200px; overflow: hidden;
    background: var(--backdrop);
  }
  .canvas {
    position: relative; width: 1200px; height: 1200px;
  }
  .front-label {
    position: absolute; left: 270px; top: 100px;
    width: 660px; height: 1000px;
    border-radius: 22px; overflow: hidden;
    background: var(--label-white);
    box-shadow: 0 10px 30px rgba(20, 25, 40, 0.18);
  }
  .label-lower {
    position: absolute; left: 0; top: 500px; width: 100%; height: 500px;
    background: var(--navy);
  }
  .label-frame {
    position: absolute; left: 22px; top: 22px; right: 22px; bottom: 22px;
    border: 4px solid var(--navy);
    border-radius: 6px;
  }
  .label-frame-inner {
    position: absolute; left: 32px; top: 32px; right: 32px; bottom: 32px;
    border: 1.5px solid var(--navy);
    border-radius: 4px;
  }
  .label-lower-frame {
    position: absolute; left: 22px; top: 500px; right: 22px; bottom: 22px;
    border: 4px solid var(--label-white);
    border-top: none;
    border-radius: 0 0 6px 6px;
  }
  .brand-top {
    position: absolute; left: 0; top: 95px; width: 100%;
    text-align: center;
    font-family: "Playfair Display", serif; font-weight: 900;
    font-size: 64px; letter-spacing: 4px;
    color: var(--navy);
  }
  .crest {
    position: absolute; left: 170px; top: 190px;
    width: 320px; height: 280px;
    border-radius: 50% 50% 46% 46%;
    background: radial-gradient(circle at 50% 45%, #e6d7a6 0%, #d5bf78 45%, #c4c6cc 75%, rgba(244,244,242,0) 100%);
  }
  .est-tag {
    position: absolute; top: 312px;
    width: 70px; height: 26px;
    background: var(--tag-grey);
    color: #fff;
    font-family: "Playfair Display", serif; font-weight: 700;
    font-size: 14px; line-height: 26px; text-align: center;
    border-bottom: 3px solid var(--gold);
  }
  .est-tag.left { left: 60px; }
  .est-tag.right { right: 60px; }
  .rope-coil {
    position: absolute; left: 120px; top: 520px;
    width: 430px; height: 170px;
    border-radius: 6px;
    background: linear-gradient(180deg, #9a9ca3 0%, var(--rope-grey) 50%, #9a9ca3 100%);
    opacity: 0.85;
  }
  .brand-bottom {
    position: absolute; left: 0; top: 705px; width: 100%;
    text-align: center;
    font-family: "Playfair Display", serif; font-weight: 700;
    font-size: 72px; letter-spacing: 1px;
    color: var(--label-white);
  }
  .sub-line {
    position: absolute; left: 0; top: 805px; width: 100%;
    text-align: center;
    font-family: "Pinyon Script", cursive;
    font-size: 46px;
    color: var(--gold);
  }
  .gold-rule {
    position: absolute; left: 120px; right: 120px; top: 885px;
    height: 2px; background: var(--gold);
  }
  .spec-row {
    position: absolute; left: 120px; right: 120px; top: 905px;
    display: flex; justify-content: space-between;
    font-family: "Oswald", sans-serif; font-weight: 500;
    font-size: 22px; color: var(--gold-soft);
    letter-spacing: 0.5px;
  }
</style>
</head>
<body>
<main class="canvas">
  <section class="front-label" aria-label="Front label">
    <div class="label-lower"></div>
    <div class="label-frame"></div>
    <div class="label-frame-inner"></div>
    <div class="label-lower-frame"></div>

    <h1 class="brand-top">HARROWMERE</h1>

    <div class="est-tag left">EST.</div>
    <div class="crest" role="img" aria-label="Heraldic crest with crown, gold lions, crossed anchors and a roped anchor roundel"></div>
    <div class="est-tag right">2018</div>

    <div class="rope-coil" role="img" aria-label="Coiled white rope laid in four horizontal rows"></div>

    <h2 class="brand-bottom">DOCK SPIRIT</h2>
    <p class="sub-line">Premium Blend</p>
    <div class="gold-rule"></div>
    <div class="spec-row">
      <span>57 % vol</span>
      <span>PRODUCT OF ENGLAND</span>
      <span>350 ml</span>
    </div>
  </section>
</main>
</body>
</html>
```